yieldcompassplans.com needs a good website design and logo

Our company sells memberships to a website that generates systematic rules-based investment strategies on a monthly basis.
I would like a modern professional wordpress design that uses the color blue. It should communicate financial safety and growth. The company is based in Denver Colorado USA.
Please see current website: https://www.yieldcompassplans.com

Target Market(s)

individual investors looking to improve their investment performance. Looking for improved returns or ways to limit losses.

Industry/Entity Type

Investment

Logo Text

yieldcompassPlans

Coding

Coded - Design and coding required

Font styles to use
Sans Serif

Colors
3176b5
85abd2
0355a3
00a990

Requirements
Must have
• I've included details in the attached document.
• The colors selected below are suggestions. While we want the color blue, please use the best version of blue you think is good.
Nice to have
• The design with work with wordpress. We would like to be able to modify the theme later using elementor and a base theme, like maybe astra?
• There is additional work to be done after this contest including designing other pages.
• The site uses some plotvanery.com to display charts and investment performance, if you have experience making these charts and graphs look good, that would be valuable.

```html
<!DOCTYPE html>
<html lang="en">
<head>
<meta charset="utf-8">
<title>yieldcompassPlans – Model Portfolios</title>
<link href="https://fonts.googleapis.com/css2?family=Montserrat:wght@400;500;600;700;800&family=Roboto:wght@400;500;700&family=Fira+Sans:wght@400&display=swap" rel="stylesheet">
<style>
:root{
  --teal:#1fd2c0;
  --violet:#4a5fe2;
  --ink:#111418;
  --muted:#555b63;
  --brand-blue:#1a2ee6;
  --card-line:#3d55e8;
  --panel-top:#0a86f2;
  --panel-bottom:#0330f2;
  --tick:#17a34a;
  --footer:#f0f0f1;
  --white:#ffffff;
}
*{box-sizing:border-box;margin:0;padding:0}
html,body{width:676px;height:1200px;overflow:hidden;background:var(--white)}
body{position:relative;font-family:"Montserrat",sans-serif;color:var(--ink)}
.abs{position:absolute}

/* hero */
.hero{left:0;top:0;width:676px;height:275px;
  background:linear-gradient(200deg,var(--teal) 0%,#2bb3d2 45%,var(--violet) 100%);
  clip-path:polygon(0 0,676px 0,676px 248px,560px 274px,0 228px)}
.brand{left:40px;top:7px;display:flex;align-items:center;gap:6px;color:var(--white);font-size:7.5px;font-weight:500}
.brand-mark{width:25px;height:25px;background:#152238;border-radius:3px}
.nav{right:18px;top:14px;display:flex;gap:19px;font-family:"Roboto",sans-serif;font-size:7px;font-weight:700;color:#0e1a2b}
.nav .active{border-bottom:1px solid #19a96b;padding-bottom:8px}
.hero-title{left:38px;top:70px;width:290px;color:var(--white);font-size:22.5px;font-weight:600;line-height:21px}
.hero-copy{left:38px;top:144px;width:260px;color:#eef4ff;font-size:6.2px;line-height:10.5px}
.hero-btn{left:38px;top:179px;width:57px;height:17px;border:1px solid #3fe0f0;color:#3fe8f5;font-size:5.5px;font-weight:600;display:flex;align-items:center;justify-content:center}
.hero-visual{left:305px;top:44px;width:360px;height:160px;border-radius:6px;
  background:linear-gradient(160deg,#3a3f47,#c9ced4 55%,#8b9098)}

/* offer */
.offer-title{left:0;top:274px;width:676px;text-align:center;font-family:"Roboto",sans-serif;font-weight:700;font-size:29px}
.offer-sub{left:0;top:308px;width:676px;text-align:center;font-family:"Roboto",sans-serif;font-size:9px;color:var(--brand-blue)}
.field{top:333px;width:89px;height:20px;border:1px solid #d6d9de;font-family:"Roboto",sans-serif;font-size:6.5px;color:#777;padding:6px 7px}
.subscribe{left:438px;top:333px;width:90px;height:20px;background:#000;color:var(--white);font-family:"Roboto",sans-serif;font-size:6.5px;font-weight:700;display:flex;align-items:center;justify-content:center}

/* features */
.photo-desk{left:0;top:396px;width:338px;height:205px;background:linear-gradient(135deg,#6b4a2e,#a98463 45%,#e6e3dc 70%,#8a6a4b)}
.photo-tablet{left:338px;top:601px;width:338px;height:212px;background:linear-gradient(120deg,#cfd1d3,#eceded 50%,#dadcde)}
.feature-text{font-family:"Fira Sans",sans-serif;font-size:12px;line-height:20px;color:#111}
.feature-one{left:361px;top:478px;width:310px}
.feature-two{left:0;top:687px;width:338px;text-align:center}

/* pricing */
.plan{text-align:center}
.plan-side{border:1px solid var(--card-line);background:var(--white)}
.plan-free{left:99px;top:875px;width:163px;height:160px;box-shadow:0 6px 20px rgba(0,0,0,.06)}
.plan-annual{left:414px;top:869px;width:150px;height:172px;box-shadow:0 6px 20px rgba(0,0,0,.06)}
.plan-monthly{left:261px;top:860px;width:153px;height:190px;color:var(--white);
  background:linear-gradient(200deg,#18d0f2 0%,var(--panel-top) 30%,var(--panel-bottom) 100%);
  box-shadow:0 10px 24px rgba(0,0,0,.18)}
.plan-name{font-size:15px;font-weight:600;margin-top:17px}
.plan-tag{font-size:5.5px;color:var(--brand-blue);margin-top:3px}
.plan-monthly .plan-tag{color:#dbe8ff}
.price{display:flex;justify-content:center;align-items:flex-start;font-weight:800;margin-top:20px;line-height:1}
.price .cur{font-size:10px;margin-top:8px}
.price .big{font-size:30px;letter-spacing:-1px}
.price .cents{font-size:8px;margin-top:7px}
.plan-note{font-size:5.5px;margin-top:6px;color:var(--muted)}
.plan-monthly .plan-note{color:#e6eeff}
.plan-list{list-style:none;margin:22px auto 0;font-size:5.5px;width:80px}
.plan-list li{display:flex;align-items:center;justify-content:center;gap:5px;height:15px}
.plan-list li+li{border-top:1px solid currentColor}
.plan-free .plan-list li+li,.plan-annual .plan-list li+li{border-top-color:#222}
.tick{width:7px;height:7px;flex:none}

/* footer */
.footer{left:0;top:1097px;width:676px;height:103px;background:var(--footer)}
.foot-nav{left:103px;top:1124px;display:flex;gap:13px;font-family:"Roboto",sans-serif;font-size:7px;font-weight:500;color:#6a6f76}
.foot-nav .active{color:#111}
.phone{right:103px;top:1124px;font-family:"Roboto",sans-serif;font-size:6.5px;font-weight:500;color:#333}
.rule{left:98px;top:1155px;width:480px;height:1px;background:#c9cbcf}
.copy{left:103px;top:1172px;font-family:"Roboto",sans-serif;font-size:5.5px;color:#555}
.social{right:103px;top:1172px;display:flex;gap:8px}
.social span{width:5px;height:5px;border-radius:50%;background:#777}
</style>
</head>
<body>

<div class="abs hero"></div>
<div class="abs brand"><span class="brand-mark"></span>yieldcompassPlans</div>
<nav class="abs nav"><span class="active">Home</span><span>Pricing</span><span>Blog</span><span>Sign Up</span><span>Login</span></nav>
<h1 class="abs hero-title">Investment strategies that boost returns and limit risk.</h1>
<p class="abs hero-copy">When you can't afford to lose, our model portfolios can protect investments by reducing holdings to risky assets when the market turns down.</p>
<div class="abs hero-btn">Learn More</div>
<div class="abs hero-visual" role="img" aria-label="Laptop showing an investment performance dashboard"></div>

<h2 class="abs offer-title">Free For a Limited Time</h2>
<p class="abs offer-sub">Stock Model Portfolios That Perform in Bear &amp; Bull Markets</p>
<div class="abs field" style="left:148px">First Name</div>
<div class="abs field" style="left:245px">Last Name</div>
<div class="abs field" style="left:342px">Your Email</div>
<div class="abs subscribe">SUBSCRIBE</div>

<div class="abs photo-desk" role="img" aria-label="Investor at a desk reviewing printed charts beside a laptop and coffee"></div>
<p class="abs feature-text feature-one">Our dynamic portfolios find the best places to invest. They adjust monthly to invest in the strongest funds.</p>
<p class="abs feature-text feature-two">You receive monthly email recommendations generated<br>from our systematic, rules-based models.</p>
<div class="abs photo-tablet" role="img" aria-label="Hands holding a tablet showing a finance report"></div>

<svg width="0" height="0" style="position:absolute">
  <defs>
    <symbol id="tick" viewBox="0 0 10 10"><circle cx="5" cy="5" r="5" fill="currentColor"/><path d="M2.8 5.2l1.5 1.5 3-3.2" fill="none" stroke="#fff" stroke-width="1.3"/></symbol>
  </defs>
</svg>

<div class="abs plan plan-side plan-free">
  <div class="plan-name">Limited Free</div>
  <div class="plan-tag">Our Introduction Package</div>
  <div class="price"><span class="cur">$</span><span class="big">0</span></div>
  <div class="plan-note">Limited Time ONLY</div>
  <ul class="plan-list" style="color:#222">
    <li><svg class="tick" style="color:var(--tick)"><use href="#tick"/></svg>Basic Strategy</li>
    <li><svg class="tick" style="color:var(--tick)"><use href="#tick"/></svg>Trends Tracker</li>
  </ul>
</div>

<div class="abs plan plan-side plan-annual">
  <div class="plan-name">Annualy</div>
  <div class="plan-tag">Best Saving</div>
  <div class="price" style="margin-top:14px"><span class="cur">$</span><span class="big">12</span><span class="cents">49</span></div>
  <div class="plan-note">per month paid annually</div>
  <ul class="plan-list" style="color:#222;margin-top:16px;width:100px">
    <li><svg class="tick" style="color:var(--tick)"><use href="#tick"/></svg>Basic Strategy</li>
    <li><svg class="tick" style="color:var(--tick)"><use href="#tick"/></svg>Trends Tracker</li>
    <li style="border-top:1px solid #222"><svg class="tick" style="color:var(--tick)"><use href="#tick"/></svg>Advanced Strategies</li>
  </ul>
</div>

<div class="abs plan plan-monthly">
  <div class="plan-name">Monthly</div>
  <div class="plan-tag">Pay as You Go</div>
  <div class="price" style="margin-top:30px"><span class="cur">$</span><span class="big">19</span><span class="cents">95</span></div>
  <div class="plan-note">per month</div>
  <ul class="plan-list" style="color:#fff;margin-top:24px;width:80px">
    <li><svg class="tick" style="color:#0a1a3a"><use href="#tick"/></svg>Basic Strategy</li>
    <li><svg class="tick" style="color:#0a1a3a"><use href="#tick"/></svg>Trends Tracker</li>
    <li><svg class="tick" style="color:#0a1a3a"><use href="#tick"/></svg>Advanced Strategies</li>
  </ul>
</div>

<footer class="abs footer"></footer>
<nav class="abs foot-nav"><span class="active">Home</span><span>Pricing</span><span>Blog</span><span>Sign Up</span><span>Login</span></nav>
<div class="abs phone">+1 303 555 0147</div>
<div class="abs rule"></div>
<div class="abs copy">© 2018 All rights Reserved.</div>
<div class="abs social"><span></span><span></span><span></span><span></span></div>

</body>
</html>
```